professional business card design for technology company

We are a small technology consulting firm, specialising in consulting based around Cloud and Managed services. Our colour scheme is yellow, blue and white, as you can see in the logos. Although we are based in melbourne australia, due to the nature of our work, our clients can be located anywhere. We are looking for a clean, professional, positive look - similar to our company logo

Target Market(s)

small business

Industry/Entity Type

Business

Contact Information for Business Card

eye catching, designed to incorporate some level of raised printing. Must contain website address, phone number, name and job title

Requirements
Must have
• Logo (attached) - use of the same colour scheme

```html
<!DOCTYPE html>
<html lang="en">
<head>
<meta charset="utf-8">
<title>Nimbara Business Card</title>
<link rel="stylesheet" href="https://fonts.googleapis.com/css2?family=Arimo:wght@400;700&display=swap">
<style>
  :root {
    --backdrop: #2f3e46;
    --card: #ffffff;
    --ink: #4a4a4a;
    --ink-dark: #3d3d3d;
    --brand-blue: #29a8e0;
    --brand-yellow: #f7d117;
  }
  * { box-sizing: border-box; margin: 0; padding: 0; }
  html, body {
    width: 1200px;
    height: 1000px;
    overflow: hidden;
    background: var(--backdrop);
    font-family: "Arimo", Arial, sans-serif;
  }
  .canvas {
    position: relative;
    width: 1200px;
    height: 1000px;
  }
  .card {
    position: absolute;
    left: 250px;
    width: 700px;
    height: 420px;
    background: var(--card);
    box-shadow: 0 10px 30px rgba(0,0,0,0.35);
  }
  .card--front { top: 40px; }
  .card--back { top: 530px; }

  .brand {
    display: flex;
    align-items: center;
    color: var(--ink);
    font-weight: 700;
    letter-spacing: -0.5px;
  }
  .brand__dot {
    border-radius: 50%;
    background: var(--brand-blue);
    flex: none;
  }
  .card--front .brand {
    position: absolute;
    left: 0; right: 0; top: 160px;
    justify-content: center;
    font-size: 84px;
    gap: 26px;
  }
  .card--front .brand__dot { width: 70px; height: 70px; }

  .card--back .brand {
    position: absolute;
    left: 50px; top: 48px;
    font-size: 54px;
    gap: 18px;
  }
  .card--back .brand__dot { width: 48px; height: 48px; }
  .website {
    position: absolute;
    left: 116px; top: 118px;
    font-size: 20px;
    color: var(--brand-blue);
    letter-spacing: 0.3px;
  }

  .contact-list {
    position: absolute;
    left: 190px; top: 188px;
    list-style: none;
  }
  .contact-list li {
    display: flex;
    align-items: center;
    gap: 10px;
    font-size: 21px;
    font-weight: 700;
    color: var(--ink-dark);
    height: 34px;
  }
  .contact-icon { width: 22px; height: 22px; flex: none; }
  .address {
    position: absolute;
    left: 186px; top: 340px;
    font-size: 21px;
    line-height: 30px;
    color: var(--ink);
  }
  .person {
    position: absolute;
    right: 60px; top: 190px;
    text-align: right;
  }
  .person__name { font-size: 22px; color: var(--ink); }
  .person__role { font-size: 18px; color: var(--brand-blue); margin-top: 6px; }
</style>
</head>
<body>
<main class="canvas">
  <section class="card card--front" aria-label="Card front">
    <div class="brand"><span class="brand__dot"></span><span class="brand__name">Nimbara</span></div>
  </section>

  <section class="card card--back" aria-label="Card back">
    <div class="brand"><span class="brand__dot"></span><span class="brand__name">Nimbara</span></div>
    <p class="website">www.nimbara.com.au</p>

    <ul class="contact-list">
      <li>
        <svg class="contact-icon" viewBox="0 0 22 22" aria-label="Mobile">
          <circle cx="11" cy="11" r="11" fill="var(--brand-blue)"/>
          <rect x="7.5" y="4.5" width="7" height="13" rx="1.5" fill="none" stroke="#fff" stroke-width="1.6"/>
        </svg>123-456-0001</li>
      <li>
        <svg class="contact-icon" viewBox="0 0 22 22" aria-label="Phone">
          <circle cx="11" cy="11" r="11" fill="var(--brand-blue)"/>
          <path d="M7 5.5c1 0 1.6 2.4 1.6 2.4l-1 1.2c.7 1.7 2 3 3.6 3.7l1.2-1s2.4.6 2.4 1.6-1 2.1-2 2.1C9 15.5 6.5 12.9 5 9.5 5 7 6 5.5 7 5.5z" fill="#fff"/>
        </svg>123-456-0002</li>
      <li>
        <svg class="contact-icon" viewBox="0 0 22 22" aria-label="Fax">
          <circle cx="11" cy="11" r="11" fill="var(--brand-blue)"/>
          <rect x="6" y="8" width="10" height="8" rx="1" fill="#fff"/>
          <rect x="8" y="5" width="6" height="3" fill="#fff"/>
          <rect x="8.5" y="10" width="5" height="1.3" fill="var(--brand-blue)"/>
        </svg>123-456-0003</li>
      <li>
        <svg class="contact-icon" viewBox="0 0 22 22" aria-label="Email">
          <circle cx="11" cy="11" r="11" fill="var(--brand-blue)"/>
          <rect x="5.5" y="7" width="11" height="8" rx="1" fill="#fff"/>
          <path d="M5.8 7.5 11 11.5l5.2-4" fill="none" stroke="var(--brand-blue)" stroke-width="1.3"/>
        </svg>name@email.com</li>
    </ul>

    <p class="address">Address line 1,<br>City, State, Zip Code</p>

    <div class="person">
      <p class="person__name">Name Goes Here</p>
      <p class="person__role">Position</p>
    </div>
  </section>
</main>
</body>
</html>
```